Redesign Non Profit Web Page

Hello

We are looking for someone to redesign our current web page. The web page is located at www.brightmerelegacy.org The final design should be creative like the following sites:

www.wellspringtide.org
http://network-for-norvale.org
http://www.topinthetown.org/

```html
<!DOCTYPE html>
<html lang="en">
<head>
<meta charset="utf-8">
<title>Brightmere Legacy</title>
<link href="https://fonts.googleapis.com/css2?family=Source+Sans+3:wght@300;400;600;700&display=swap" rel="stylesheet">
<style>
:root{
  --teal:#1f9a85;
  --teal-dark:#157a6a;
  --teal-bright:#2bb39a;
  --ink:#333;
  --muted:#666;
  --footer-bg:#ececec;
}
*{box-sizing:border-box;margin:0;padding:0}
html,body{width:1015px;height:1200px;overflow:hidden}
body{font-family:"Source Sans 3",Arial,sans-serif;color:var(--ink);background:#fff;position:relative}
a{color:inherit;text-decoration:none}
.abs{position:absolute}

.site-header{position:absolute;left:0;top:0;width:1015px;height:115px;background:linear-gradient(#fff 0,#fff 50%,#f3f3f3 50%,#f1f1f1 100%)}
.brand{position:absolute;left:86px;top:36px;font-size:31px;font-weight:600;color:var(--teal-dark);letter-spacing:-.3px;line-height:1}
.donate{left:619px;top:18px;width:117px;height:24px;background:var(--teal-dark);color:#fff;font-weight:700;font-size:13px;text-align:center;line-height:24px;letter-spacing:.5px}
.search{left:751px;top:18px;width:179px;height:24px;border:1px solid #ccc;background:#fff;font-size:12px;color:#555;padding-left:12px;line-height:22px}
.search svg{position:absolute;right:7px;top:5px}
.main-nav{left:618px;top:80px;display:flex;gap:30px;font-size:14px;color:#333}
.main-nav .current{color:var(--teal)}

.hero{left:0;top:115px;width:1015px;height:297px;background:#111}
.hero-photo{position:absolute;left:0;top:0;width:560px;height:297px;background:linear-gradient(90deg,#7d7670 0%,#9a8a7c 25%,#5e4b3f 60%,#1a1a1a 100%)}
.hero-copy{position:absolute;right:85px;top:65px;text-align:right}
.hero-title{font-weight:300;color:#fff;font-size:37px;letter-spacing:.5px;line-height:1}
.hero-sub{font-weight:600;color:var(--teal-bright);font-size:20px;margin-top:12px;letter-spacing:.3px}
.hero-btn{display:inline-block;margin-top:14px;width:180px;height:40px;background:#fff;border-radius:2px;color:#333;font-size:16px;line-height:40px;text-align:center}
.dots{position:absolute;left:856px;top:265px;display:flex;gap:8px}
.dots i{width:12px;height:12px;border-radius:50%;background:#bbb;display:block}
.dots i:first-child{background:#444;border:1px solid #999}

.welcome{left:85px;top:432px;width:847px;text-align:center}
.welcome h1{font-weight:300;font-size:29px;color:var(--teal);letter-spacing:.3px}
.welcome p{width:780px;margin:12px auto 0;font-size:15.5px;line-height:24.5px;color:var(--muted)}
.welcome .more{font-size:11.5px;font-weight:700;color:#333;margin-left:6px}
.rule{left:85px;top:579px;width:847px;height:1px;background:#ddd}

.card{top:604px;width:265px}
.card-img{height:161px}
.card-label{margin-top:3px;height:40px;background:repeating-linear-gradient(135deg,var(--teal-bright) 0 3px,#27a88f 3px 5px);color:#fff;font-weight:700;font-size:21px;text-align:center;line-height:40px;letter-spacing:.5px}

.event{left:93px;top:831px;width:829px;height:85px;background:repeating-linear-gradient(135deg,#333 0 3px,#2a2a2a 3px 5px)}
.event-head{position:absolute;left:0;top:0;width:197px;height:85px;text-align:center;color:#fff}
.event-head svg{margin-top:15px}
.event-head h2{font-size:19px;font-weight:700;letter-spacing:.5px;margin-top:4px}
.event-div{position:absolute;left:197px;top:8px}
.event-text{position:absolute;left:235px;top:22px;color:#fff;font-size:13.5px}
.event-text time{display:block;margin-top:9px;color:#bbb;font-size:12.5px}

.site-footer{left:0;top:943px;width:1015px;height:207px;background:var(--footer-bg);border-top:1px solid #ddd}
.fcol{position:absolute;top:22px}
.fcol h3{font-size:13px;font-weight:600;color:var(--teal);margin-bottom:9px}
.fcol li{list-style:none;font-size:11.5px;color:#555;line-height:17.6px}
.bottom-bar{left:0;top:1150px;width:1015px;height:50px;background:linear-gradient(#3a3a3a,#232323);color:#ddd;font-size:11.5px}
.bottom-bar p{position:absolute;left:86px;top:18px}
.social{position:absolute;left:820px;top:14px;display:flex;gap:8px}
.social span{width:21px;height:21px;border-radius:50%;background:#777;display:block}
</style>
</head>
<body>

<header class="site-header">
  <div class="brand">Brightmere Legacy</div>
  <a class="abs donate" href="#">DONATE NOW</a>
  <div class="abs search">Search
    <svg width="13" height="13" viewBox="0 0 13 13"><circle cx="5" cy="5" r="3.8" fill="none" stroke="#222" stroke-width="2"/><line x1="8" y1="8" x2="12" y2="12" stroke="#222" stroke-width="2.4"/></svg>
  </div>
  <nav class="abs main-nav">
    <a class="current" href="#">Home</a><a href="#">About</a><a href="#">Forms</a><a href="#">Events</a><a href="#">Contact</a>
  </nav>
</header>

<section class="abs hero">
  <div class="hero-photo" role="img" aria-label="Portrait photograph of a young girl leaning against a tree"></div>
  <div class="hero-copy">
    <div class="hero-title">“TRANSFORMING LIVES”</div>
    <div class="hero-sub">SUCCESS IS A JOURNEYNOT A DESTINATION</div>
    <a class="hero-btn" href="#">BECOME A VOLUNTEER</a>
  </div>
  <div class="dots"><i></i><i></i><i></i><i></i></div>
</section>

<section class="abs welcome">
  <h1>WELCOME TO BRIGHTMERE LEGACY</h1>
  <p>It is a 501(c)(3) non-profit educational organization dedicated to Transforming Lives! Brightmere Legacy’s Mission is to develop systemic approaches to enhance family economic security, encourage individual achievement and promote empowerment of self-sufficiency. <a class="more" href="#">KNOW MORE &#9656;</a></p>
</section>
<div class="abs rule"></div>

<a class="abs card" style="left:93px" href="#">
  <div class="card-img" role="img" aria-label="Photograph of two schoolgirls reading a book" style="background:linear-gradient(135deg,#cfd8e2,#8fb6d6 60%,#c99a6e)"></div>
  <div class="card-label">WHAT WE DO</div>
</a>
<a class="abs card" style="left:375px" href="#">
  <div class="card-img" role="img" aria-label="Photograph of hands holding a small tree seedling" style="background:linear-gradient(#a9cbe6 0%,#dbe9f2 55%,#9bb86a 100%)"></div>
  <div class="card-label">THE IMPACT</div>
</a>
<a class="abs card" style="left:658px" href="#">
  <div class="card-img" role="img" aria-label="Photograph of many hands joined together in a circle" style="background:radial-gradient(circle at 50% 50%,#b9876a,#8a6448 55%,#c7a27a)"></div>
  <div class="card-label">WHAT YOU CAN DO</div>
</a>

<section class="abs event">
  <div class="event-head">
    <svg width="28" height="28" viewBox="0 0 28 28"><rect x="2" y="4" width="24" height="22" rx="2" fill="none" stroke="#fff" stroke-width="2"/><rect x="2" y="4" width="24" height="6" fill="#fff"/><rect x="7" y="1" width="3" height="6" fill="#fff"/><rect x="18" y="1" width="3" height="6" fill="#fff"/><text x="14" y="22" font-size="9" fill="#fff" text-anchor="middle" font-family="Arial,sans-serif">12</text></svg>
    <h2>LATEST EVENT</h2>
  </div>
  <svg class="event-div" width="14" height="70" viewBox="0 0 14 70"><polyline points="1,0 1,27 10,35 1,43 1,70" fill="none" stroke="#777" stroke-width="1"/></svg>
  <div class="event-text">Fusce hendrerit quam sed tempor malesuadaeuismod dolor nec velit cursus, in volutpat risus bibendum.
    <time>October - 15 - 2013</time></div>
</section>

<footer class="abs site-footer">
  <div class="fcol" style="left:94px"><h3>About</h3><ul><li>Our Mission &amp; Vision</li><li>Board of Directors</li><li>Staff</li><li>Internships</li></ul></div>
  <div class="fcol" style="left:231px"><h3>Forms &amp; Links</h3><ul><li>Forms</li><li>Links</li><li>Video Gallery</li><li>Picture Gallery</li></ul></div>
  <div class="fcol" style="left:356px"><h3>What We Do</h3><ul><li>Arts &amp; Humanities</li><li>Community Development</li><li>Education</li><li>Employment, Labor &amp; Training</li><li>Food &amp; Nutrition</li><li>Housing</li><li>Law &amp; Justice Services</li><li>Transportation</li></ul></div>
  <div class="fcol" style="left:545px"><h3>The Impact</h3><ul><li>The Numbers</li><li>Annual Report</li></ul></div>
  <div class="fcol" style="left:665px"><h3>What You Can Do</h3><ul><li>Donate</li><li>Volunteer</li><li>Become a Mentor</li><li>Corporate Sponsorship</li><li>Share Your Story</li></ul></div>
  <div class="fcol" style="left:819px"><h3>Terms &amp; Privacy</h3><ul><li>Terms and Conditions</li><li>Privacy Statement</li></ul></div>
</footer>

<div class="abs bottom-bar">
  <p>Copyright &copy; 2013 &nbsp;Brightmere Legacy Foundation. &nbsp;&nbsp;All rights reserved.</p>
  <div class="social"><span></span><span></span><span></span><span></span></div>
</div>

</body>
</html>
```